Marlowe Holdings LLC - Business Cards

Need the following information on the cards:

Name: Dean R Vossler
Title: Chief Executive Manager

Business address:
412 N Ridgeview Lane #118
Alder Grove, Il 60412

Phone: (630) 555-0148 - Business
KPV FFL license number: 5-21-xxx-xx-xx-04519
Email: dean.vossler@marloweholdingsffl.com

Target Market(s)

Firearm owners

Industry/Entity Type

Firearms industry,

Contact Information for Business Card

Contact number, name and title, web page address, email, business address and kpv license number,

Requirements
Must have
• Name, title, business address, phone numbers, KPV license numbers, web page address and email address.
Nice to have
• Cellphone number,

```html
<!DOCTYPE html>
<html lang="en">
<head>
<meta charset="UTF-8">
<title>Marlowe Holdings LLC – Business Cards</title>
<link href="https://fonts.googleapis.com/css2?family=Cinzel:wght@700&family=Montserrat:wght@500&family=Roboto:wght@400&display=swap" rel="stylesheet">
<style>
  :root {
    --backdrop: #232323;
    --red: #c8161e;
    --red-deep: #9c0f15;
    --black: #0b0b0b;
    --white: #f2f2f0;
    --text-light: #ffffff;
  }
  html, body {
    margin: 0;
    padding: 0;
    width: 1200px;
    height: 880px;
    overflow: hidden;
    background: var(--backdrop);
  }
  .canvas {
    position: relative;
    width: 1200px;
    height: 880px;
  }
  .card {
    position: absolute;
    left: 296px;
    width: 608px;
    height: 348px;
    overflow: hidden;
    background: var(--red);
  }
  .card--front { top: 81px; }
  .card--back { top: 452px; background: var(--black); }
  .card-shapes {
    position: absolute;
    inset: 0;
    width: 608px;
    height: 348px;
  }
  .brand-name {
    position: absolute;
    font-family: "Cinzel", serif;
    font-weight: 700;
    color: var(--red);
    text-align: center;
    line-height: 1.1;
  }
  .card--front .brand-name {
    left: 175px;
    top: 140px;
    width: 258px;
    font-size: 32px;
  }
  .card--back .brand-name {
    left: 350px;
    top: 102px;
    width: 200px;
    font-size: 21px;
  }
  .contact-list {
    position: absolute;
    left: 49px;
    top: 93px;
    margin: 0;
    padding: 0;
    list-style: none;
    font-family: "Roboto", sans-serif;
    color: var(--text-light);
  }
  .contact-item {
    position: relative;
    padding-left: 42px;
    min-height: 30px;
    margin-bottom: 10px;
  }
  .contact-item--address { margin-top: 4px; }
  .contact-icon {
    position: absolute;
    left: 0;
    top: 1px;
    width: 30px;
    height: 30px;
  }
  .contact-label {
    display: block;
    font-size: 8px;
    line-height: 10px;
  }
  .contact-value {
    display: block;
    font-size: 11px;
    line-height: 14px;
  }
  .contact-value--large { font-size: 13px; line-height: 15px; }
  .person {
    position: absolute;
    left: 300px;
    width: 300px;
    top: 190px;
    text-align: center;
  }
  .person-name {
    margin: 0;
    font-family: "Cinzel", serif;
    font-weight: 700;
    font-size: 25px;
    line-height: 28px;
    color: var(--red);
  }
  .person-title {
    margin: 2px 0 0;
    font-family: "Montserrat", sans-serif;
    font-weight: 500;
    font-size: 14px;
    letter-spacing: 1.6px;
    color: var(--text-light);
  }
</style>
</head>
<body>
<main class="canvas">

  <section class="card card--front" aria-label="Business card front">
    <svg class="card-shapes" viewBox="0 0 608 348" aria-hidden="true">
      <defs>
        <linearGradient id="frontRed" x1="0" y1="0" x2="1" y2="1">
          <stop offset="0" stop-color="#d71a22"/>
          <stop offset="1" stop-color="#b31118"/>
        </linearGradient>
      </defs>
      <rect width="608" height="348" fill="url(#frontRed)"/>
      <path d="M336 0 C250 120 270 260 372 348 L608 348 L608 0 Z" fill="var(--black)"/>
      <circle cx="304" cy="178" r="139" fill="var(--white)"/>
    </svg>
    <div class="brand-name">Marlowe Holdings LLC</div>
  </section>

  <section class="card card--back" aria-label="Business card back">
    <svg class="card-shapes" viewBox="0 0 608 348" aria-hidden="true">
      <path d="M0 0 L228 0 C350 80 352 270 220 348 L0 348 Z" fill="var(--red-deep)"/>
      <path d="M0 0 L210 0 C330 80 332 270 200 348 L0 348 Z" fill="var(--red)"/>
    </svg>

    <ul class="contact-list">
      <li class="contact-item">
        <svg class="contact-icon" viewBox="0 0 30 30" aria-hidden="true">
          <circle cx="15" cy="15" r="15" fill="var(--black)"/>
          <path d="M10 8 l3 -1 l2 4 l-2 2 q1 3 4 4 l2 -2 l4 2 l-1 3 q-8 1 -12 -12 z" fill="none" stroke="#fff" stroke-width="1.4"/>
        </svg>
        <span class="contact-label">Business</span>
        <span class="contact-value contact-value--large">(630) 555-0148</span>
      </li>
      <li class="contact-item">
        <svg class="contact-icon" viewBox="0 0 30 30" aria-hidden="true">
          <circle cx="15" cy="15" r="15" fill="var(--black)"/>
          <path d="M7 15 L23 8 L19 23 L15 18 Z" fill="#fff"/>
        </svg>
        <span class="contact-label">Email</span>
        <span class="contact-value">dean.vossler@marloweholdingsffl.com</span>
      </li>
      <li class="contact-item">
        <svg class="contact-icon" viewBox="0 0 30 30" aria-hidden="true">
          <circle cx="15" cy="15" r="15" fill="var(--black)"/>
          <rect x="8" y="9" width="14" height="12" fill="none" stroke="#fff" stroke-width="1.3"/>
          <path d="M10 12 h6 M10 15 h6 M10 18 h6" stroke="#fff" stroke-width="1.1"/>
          <circle cx="19" cy="14" r="1.6" fill="#fff"/>
        </svg>
        <span class="contact-label">KPV FFL license number</span>
        <span class="contact-value">5-21-XXX-XX-XX-04519</span>
      </li>
      <li class="contact-item contact-item--address">
        <svg class="contact-icon" viewBox="0 0 30 30" aria-hidden="true">
          <circle cx="15" cy="15" r="15" fill="var(--black)"/>
          <path d="M15 24 C10 17 9 15 9 13 a6 6 0 0 1 12 0 c0 2 -1 4 -6 11 z" fill="#fff"/>
          <circle cx="15" cy="13" r="2.3" fill="var(--black)"/>
        </svg>
        <span class="contact-label">Business address</span>
        <span class="contact-value">412 N Ridgeview Lane #118</span>
        <span class="contact-value">Alder Grove, Il 60412</span>
      </li>
    </ul>

    <div class="brand-name">Marlowe Holdings LLC</div>

    <div class="person">
      <h1 class="person-name">DEAN R VOSSLER</h1>
      <p class="person-title">CHIEF EXECUTIVE MANAGER</p>
    </div>
  </section>

</main>
</body>
</html>
```